Info Graphic about Maple Ridge Restaurant

This info graphic should detail all releavent details about Maple Ridge, such as opening hours, accepted payment methods, home delivery areas etc. please refer attached word document for details.

Also attached a pdf with old info graphic.

IMPORTANT:. Given there is lot of text, I expect the designer to make this interesting. This will be printed in A1 and also A4
Also, I need this in both Portrait and landscape designs.

Industry/Entity Type

Hospitality

Font styles to use
Serif
Sans Serif
Decorative
Script
Other font styles liked:
• I let designer choose

Colors

Designer to choose colors to be used in the design.

Requirements
Must have
• Refer attached word doc
Nice to have
• Refer attached word doc
Should not have
• Refer attached word doc

```html
<!DOCTYPE html>
<html lang="en">
<head>
<meta charset="utf-8">
<title>Maple Ridge Indian Restaurant – Info Sheet</title>
<link rel="stylesheet" href="https://fonts.googleapis.com/css2?family=Roboto+Condensed:wght@300;400;500;700;900&family=Roboto:wght@400;500;700;900&display=swap">
<style>
  :root {
    --red: #e8262b;
    --red-dark: #9b1b1f;
    --maroon: #8a1a1c;
    --pale-yellow: #fbf06a;
    --orange: #f9b21c;
    --green: #9ccb3b;
    --purple: #7a63a8;
    --olive: #c3b735;
    --ink: #111;
    --grey-text: #444;
    --white: #fff;
    --accent-orange: #e4572e;
    --gold-text: #ffd43b;
  }
  html, body { margin: 0; padding: 0; overflow: hidden; }
  body { background: #fff; }
  .canvas {
    position: relative; width: 847px; height: 1200px; overflow: hidden;
    background: var(--white); font-family: "Roboto", sans-serif; color: var(--ink);
  }
  .abs { position: absolute; }
  .circle { position: absolute; border-radius: 50%; }
  .circle--yellow { left: 440px; top: 0; width: 528px; height: 528px; background: var(--pale-yellow); }
  .circle--red { left: -100px; top: -44px; width: 568px; height: 568px; background: var(--red); }
  .circle--orange { left: 384px; top: 376px; width: 432px; height: 432px; background: var(--orange); }
  .circle--green { left: 520px; top: 784px; width: 440px; height: 440px; background: var(--green); }
  .circle--cloche { left: 626px; top: 784px; width: 98px; height: 98px; background: var(--purple); }

  /* header plate */
  .plate {
    position: absolute; left: 124px; top: 12px; width: 628px; height: 184px; border-radius: 50%;
    background: linear-gradient(180deg, #fafafa, #d9d9d9); box-shadow: 0 4px 8px rgba(0,0,0,.25);
  }
  .plate__screw { position: absolute; top: 84px; width: 22px; height: 22px; border-radius: 50%;
    background: linear-gradient(135deg, #fff, #aaa); }
  .plate__screw--left { left: 22px; } .plate__screw--right { right: 22px; }
  .chillies { position: absolute; top: 24px; width: 104px; height: 150px; border-radius: 40% 40% 50% 50%;
    background: linear-gradient(90deg, #c81d22, #e8262b 35%, #f07a22 65%, #e9c43a); }
  .chillies--left { left: 184px; } .chillies--right { left: 598px; }
  .brand { position: absolute; left: 290px; width: 306px; text-align: center;
    font-family: "Roboto Condensed", sans-serif; font-weight: 700; color: var(--maroon); }
  .brand__name { top: 50px; font-size: 46px; }
  .brand__tag { top: 110px; font-size: 30px; }

  /* opening hours */
  .hours__title { left: 34px; top: 212px; margin: 0; font-family: "Roboto Condensed", sans-serif; font-weight: 700;
    font-size: 44px; color: var(--white); letter-spacing: .5px; }
  .hours__band { position: absolute; left: 0; width: 444px; background: var(--red-dark); color: var(--white);
    font-family: "Roboto Condensed", sans-serif; font-weight: 500; }
  .hours__band--weekday { top: 266px; height: 72px; }
  .hours__band--weekend { top: 340px; height: 64px; }
  .hours__days { position: absolute; left: 38px; font-size: 31px; }
  .hours__days small { font-size: 18px; }
  .hours__times { position: absolute; left: 38px; font-size: 18px; word-spacing: 2px; }
  .hours__band--weekday .hours__days { top: 4px; } .hours__band--weekday .hours__times { top: 46px; }
  .hours__band--weekend .hours__days { top: 2px; } .hours__band--weekend .hours__times { top: 38px; }
  .buffet { left: 28px; width: 370px; top: 414px; text-align: center; color: var(--white);
    font-family: "Roboto Condensed", sans-serif; }
  .buffet__line1 { font-size: 14px; font-weight: 700; }
  .buffet__line1 b { font-size: 23px; }
  .buffet__line2 { font-size: 19px; margin-top: 4px; }
  .buffet__line2 small { font-size: 13px; }

  /* bookings */
  .booking { left: 480px; top: 212px; font-family: "Roboto Condensed", sans-serif; font-weight: 700; }
  .booking__title { font-size: 42px; color: var(--red); line-height: 1; }
  .booking__phone { font-family: "Roboto", sans-serif; font-size: 28px; color: var(--maroon); margin-top: 12px; }
  .booking__link { font-size: 22px; color: var(--maroon); margin-top: 4px; }

  /* delivery */
  .rider { left: 656px; top: 396px; width: 172px; height: 172px; border-radius: 30% 30% 40% 40%;
    background: linear-gradient(160deg, #e24a4a, #d83a3a 50%, #f2d6b0); }
  .delivery__head { left: 444px; top: 428px; width: 210px; transform: rotate(-12deg); transform-origin: left top;
    font-family: "Roboto Condensed", sans-serif; font-weight: 900; font-size: 42px; line-height: .95;
    color: var(--red); -webkit-text-stroke: 1.5px var(--white); text-align: center; }
  .delivery__fees { left: 428px; top: 540px; transform: rotate(-12deg); transform-origin: left top;
    font-family: "Roboto Condensed", sans-serif; font-weight: 700; font-size: 19px; color: var(--ink); line-height: 1.2; }
  .delivery__fees .line1 { padding-left: 40px; }
  .delivery__fee-badge { display: inline-block; width: 34px; height: 34px; border-radius: 50%; background: var(--red);
    color: var(--white); text-align: center; line-height: 34px; font-size: 18px; margin-left: 2px; }
  .delivery__fees .line2 { border-bottom: 3px solid var(--red-dark); padding-bottom: 2px; }
  .suburbs { position: absolute; top: 606px; list-style: none; margin: 0; padding: 0;
    font-family: "Roboto Condensed", sans-serif; font-size: 18px; line-height: 23.4px; color: #1a1a1a; }
  .suburbs li::before { content: ""; display: inline-block; width: 11px; height: 11px; border-radius: 50%;
    background: var(--red); margin-right: 8px; vertical-align: 1px; }
  .suburbs--a { left: 474px; } .suburbs--b { left: 606px; }

  /* payments */
  .payment__title { left: 58px; top: 534px; font-family: "Roboto", sans-serif; font-size: 32px; }
  .payment__title b { font-weight: 900; } .payment__title span { font-weight: 400; }
  .terminal { left: 62px; top: 566px; width: 146px; height: 170px; border-radius: 14px;
    background: linear-gradient(180deg, #e9e9e9 0 18%, #4b4f56 18%); }
  .surcharge { left: 68px; top: 746px; font-family: "Roboto Condensed", sans-serif; font-size: 16px;
    line-height: 1.3; color: var(--accent-orange); }
  .accept { left: 224px; top: 576px; width: 150px; height: 210px; border: 3px solid var(--ink); background: var(--white);
    font-family: "Roboto Condensed", sans-serif; }
  .accept__head { background: var(--olive); color: var(--white); font-size: 20px; font-weight: 500; padding: 4px 0 4px 10px; }
  .accept__list { list-style: none; margin: 4px 0 0; padding: 0 0 0 8px; font-size: 15.5px; line-height: 20px; font-weight: 500; }
  .accept__list li { position: relative; padding-left: 18px; }
  .accept__list li::before { content: "✔"; position: absolute; left: 0; color: var(--olive); font-size: 13px; }
  .accept__no { margin-top: 4px; background: var(--red); color: var(--white); font-size: 20px; font-weight: 500; padding: 3px 0 3px 10px; }
  .accept__reject { padding: 8px 0 0 10px; font-size: 15px; font-weight: 700; }
  .accept__reject span { color: var(--red); margin-right: 4px; }

  /* vouchers */
  .vouchers__title { left: 34px; top: 812px; font-family: "Roboto Condensed", sans-serif; font-size: 58px; line-height: 1; }
  .vouchers__title b { color: var(--red); font-weight: 700; } .vouchers__title span { font-weight: 300; }
  .voucher-art { left: 36px; top: 878px; width: 132px; height: 114px;
    background: linear-gradient(135deg, #6d2a16, #b5521f 55%, #e07b2a); border-radius: 4px; }
  .vouchers__copy { left: 216px; top: 886px; width: 270px; font-family: "Roboto Condensed", sans-serif;
    font-weight: 700; font-size: 15.5px; line-height: 19px; color: var(--grey-text); }
  .vouchers__copy p { margin: 0 0 19px; }
  .nowrap { white-space: nowrap; }

  /* services */
  .cloche-icon { left: 636px; top: 800px; width: 78px; height: 60px; border-radius: 40px 40px 10px 10px;
    background: linear-gradient(180deg, #d8d8d8, #8f8f8f); }
  .services__title { left: 568px; top: 880px; font-family: "Roboto Condensed", sans-serif; font-weight: 700;
    font-size: 56px; color: var(--white); }
  .services__list { position: absolute; left: 566px; top: 952px; list-style: none; margin: 0; padding: 0;
    font-family: "Roboto Condensed", sans-serif; font-size: 24px; line-height: 31px; color: #1a1a1a; }
  .services__list li::before { content: ""; display: inline-block; width: 11px; height: 11px; border-radius: 50%;
    background: var(--red); margin-right: 12px; vertical-align: 4px; }

  /* byo band */
  .byo { left: 0; top: 1022px; width: 544px; height: 90px; background: var(--red); color: var(--white);
    font-family: "Roboto Condensed", sans-serif; }
  .byo__title { position: absolute; left: 44px; top: 8px; font-weight: 700; font-size: 28px; }
  .byo__note { position: absolute; left: 44px; top: 44px; font-size: 16px; }
  .byo__warn { position: absolute; left: 42px; top: 64px; font-weight: 700; font-size: 20px; color: var(--gold-text); }

  /* footer */
  .footer { left: 0; top: 1112px; width: 847px; height: 88px; background: var(--white); }
  .footer__web { position: absolute; left: 40px; top: 14px; font-family: "Roboto", sans-serif; font-weight: 700;
    font-size: 40px; color: var(--red); white-space: nowrap; }
  .badge { position: absolute; top: 10px; width: 64px; height: 64px; }
  .badge--gold { left: 570px; border-radius: 50%; background: radial-gradient(circle, #d6a93a, #9a7419); }
  .badge--ring { left: 648px; border-radius: 50%; border: 3px solid #5bb58a; box-sizing: border-box; }
  .badge--diamond { left: 728px; width: 50px; height: 50px; top: 17px; transform: rotate(45deg); background: #2f9fc1; }
</style>
</head>
<body>
<main class="canvas">
  <div class="circle circle--yellow"></div>
  <div class="circle circle--red"></div>
  <div class="circle circle--orange"></div>
  <div class="circle circle--green"></div>

  <header class="plate">
    <span class="plate__screw plate__screw--left"></span>
    <span class="plate__screw plate__screw--right"></span>
  </header>
  <div class="chillies chillies--left" role="img" aria-label="Bunch of red, orange and yellow chillies"></div>
  <div class="chillies chillies--right" role="img" aria-label="Bunch of red, orange and yellow chillies"></div>
  <div class="brand brand__name">Maple Ridge</div>
  <div class="brand brand__tag">Indian Restaurant</div>

  <section>
    <h2 class="abs hours__title">OPENING HOURS</h2>
    <div class="hours__band hours__band--weekday">
      <div class="hours__days">MONDAY <small>TO</small> FRIDAY</div>
      <div class="hours__times">11:30AM - 2:30PM &nbsp;&nbsp;5:00PM – 9:00PM</div>
    </div>
    <div class="hours__band hours__band--weekend">
      <div class="hours__days">SATURDAY <small>TO</small> SUNDAY</div>
      <div class="hours__times">10:30AM - 2:30PM &nbsp;&nbsp;5:00PM – 9:00PM</div>
    </div>
    <div class="abs buffet">
      <div class="buffet__line1"><b>DINNER BUFFET</b> IS AVAILABLE ONLY FROM</div>
      <div class="buffet__line2">MON-THU <small>FROM</small> 5:30PM-8:30PM</div>
    </div>
  </section>

  <section class="abs booking">
    <div class="booking__title">BOOKING ORDERS</div>
    <div class="booking__phone">08 5550 0142</div>
    <div class="booking__link">admin@mapleridge.com.au</div>
    <div class="booking__link">www.mapleridge.com.au</div>
  </section>

  <section>
    <div class="abs rider" role="img" aria-label="Delivery rider on a red scooter with a food delivery box"></div>
    <div class="abs delivery__head">Suburbs we deliver to</div>
    <div class="abs delivery__fees">
      <div class="line1">Delivery Charges <span class="delivery__fee-badge">$5</span></div>
      <div class="line2">minimum order value $30</div>
    </div>
    <ul class="suburbs suburbs--a">
      <li>Beldon</li><li>Craigie</li><li>Darch</li><li>Duncraig</li><li>Edgewater</li><li>Greenwood</li>
    </ul>
    <ul class="suburbs suburbs--b">
      <li>Hocking</li><li>Kingsley</li><li>Madeley</li><li>Padbury</li><li>Pearsall</li><li>Wangara</li><li>Woodvale</li>
    </ul>
  </section>

  <section>
    <div class="abs payment__title"><b>PAYMENT</b> <span>METHODS</span></div>
    <div class="abs terminal" role="img" aria-label="Card payment terminal with receipt and card"></div>
    <div class="abs surcharge">SURCHARGE<br>OF 2.8% APPLY</div>
    <div class="abs accept">
      <div class="accept__head">WE ACCEPT</div>
      <ul class="accept__list">
        <li>Cash</li><li>All Australian EFTPOS</li><li>Debit</li><li>Credit Cards</li>
      </ul>
      <div class="accept__no">NOT ACCEPT</div>
      <div class="accept__reject"><span>X</span>REGENT CLUB</div>
    </div>
  </section>

  <section>
    <div class="abs vouchers__title"><b>DISCOUNT</b> <span>VOUCHERS</span></div>
    <div class="abs voucher-art" role="img" aria-label="Two restaurant discount voucher cards"></div>
    <div class="abs vouchers__copy">
      <p>We accept Saver Book Vouchers<br>and Maple Ridge supplied<br>Discount vouchers.</p>
      <p>Saver Vouchers are eligible only<br>for <span class="nowrap">Dine-In.</span></p>
    </div>
  </section>

  <div class="circle circle--cloche"></div>
  <div class="abs cloche-icon" role="img" aria-label="Serving cloche held on a hand"></div>
  <section>
    <div class="abs services__title">Services</div>
    <ul class="services__list">
      <li>Functions/Parties</li><li>Bulk Cooking</li><li>Special Orders</li><li>Business Meetings</li><li>Seminars/Presentations</li>
    </ul>
  </section>

  <section class="abs byo">
    <div class="byo__title">BYO allowed only for Wine.</div>
    <div class="byo__note">Charges per bottle apply</div>
    <div class="byo__warn">* OUTSIDE FOOD IS NOT ALLOWED!</div>
  </section>

  <footer class="abs footer">
    <div class="footer__web">www.mapleridge.com.au</div>
    <div class="badge badge--gold" role="img" aria-label="Award badge"></div>
    <div class="badge badge--ring" role="img" aria-label="Certificate badge"></div>
    <div class="badge badge--diamond" role="img" aria-label="Diners award badge"></div>
  </footer>
</main>
</body>
</html>
```